Business Card Design

We need a design for business cards for our company. We have a logo. We teach EMT's and we are based out of Virginia. The information that will need to add would be, name, title, phone number, email, address. On the back of the business card would be "We help you, help others"

Target Market(s)

People that want to become EMT's

Colors

Designer to choose colors to be used in the design.

Requirements
Must have
• company logo

```html
<!DOCTYPE html>
<html lang="en">
<head>
<meta charset="UTF-8">
<title>Medicrew Training – Business Card</title>
<link href="https://fonts.googleapis.com/css2?family=Work+Sans:wght@400;500&display=swap" rel="stylesheet">
<style>
  :root {
    --stage: #1e1e1e;
    --card-dark: #2b2b2b;
    --card-light: #ffffff;
    --brand-red: #c8202f;
    --text-grey: #7a7a7a;
    --emboss: #4a4a4a;
    --emboss-light: #5c5c5c;
  }
  * { margin: 0; padding: 0; box-sizing: border-box; }
  html, body {
    width: 1200px; height: 878px; overflow: hidden;
    background: var(--stage);
    font-family: "Work Sans", sans-serif;
  }
  .stage {
    width: 1200px; height: 878px;
    display: flex; flex-direction: column;
    align-items: center; justify-content: center; gap: 56px;
  }
  .card {
    position: relative;
    width: 560px; height: 320px;
    box-shadow: 0 10px 30px rgba(0,0,0,0.45);
  }
  /* Back */
  .card--back {
    background: var(--card-dark);
    display: flex; align-items: center; justify-content: center;
  }
  .wordmark--emboss {
    display: flex; align-items: center; gap: 12px;
    font-weight: 500; font-size: 30px; letter-spacing: 1px;
    color: var(--emboss);
    text-transform: uppercase;
  }
  .wordmark--emboss .mark {
    width: 18px; height: 18px; border-radius: 50%;
    background: var(--emboss-light);
  }
  /* Front */
  .card--front { background: var(--card-light); }
  .wordmark--front {
    position: absolute; top: 34px; right: 32px;
    display: flex; align-items: center; gap: 9px;
    font-weight: 500; font-size: 22px; letter-spacing: 0.5px;
    color: var(--brand-red);
    text-transform: uppercase;
  }
  .wordmark--front .mark {
    width: 12px; height: 12px; border-radius: 50%;
    background: var(--brand-red);
  }
  .identity {
    position: absolute; top: 122px; left: 0;
    padding-left: 34px;
  }
  .identity::before {
    content: ""; position: absolute; left: 0; top: 2px;
    width: 12px; height: 40px; background: var(--brand-red);
  }
  .identity__name {
    font-weight: 500; font-size: 20px; letter-spacing: 1px;
    color: var(--brand-red); text-transform: uppercase;
  }
  .identity__title {
    font-size: 12px; color: var(--text-grey); letter-spacing: 0.5px;
    margin-top: 2px;
  }
  .divider {
    position: absolute; top: 182px; left: 24px; right: 48px;
    height: 1px; background: var(--brand-red);
  }
  .contacts {
    position: absolute; top: 204px; left: 28px;
    list-style: none;
    font-size: 13px; color: var(--text-grey); letter-spacing: 0.5px;
  }
  .contacts li { display: flex; align-items: center; gap: 9px; height: 21px; }
  .contacts svg { width: 10px; height: 10px; flex: none; }
  .contacts .accent { color: var(--brand-red); }
  .address {
    position: absolute; bottom: 28px; right: 48px;
    text-align: right; font-size: 13px; line-height: 1.45;
    color: var(--text-grey); letter-spacing: 0.6px; font-style: normal;
  }
</style>
</head>
<body>
<main class="stage">
  <section class="card card--back" aria-label="Card back">
    <div class="wordmark--emboss"><span class="mark"></span>Medicrew Training</div>
  </section>

  <section class="card card--front" aria-label="Card front">
    <div class="wordmark--front"><span class="mark"></span>Medicrew Training</div>

    <div class="identity">
      <h1 class="identity__name">Daniel Reyes</h1>
      <p class="identity__title">Director</p>
    </div>

    <div class="divider"></div>

    <ul class="contacts">
      <li>
        <svg viewBox="0 0 10 10" aria-hidden="true"><path d="M2 0.5 L4 2.5 L3 4 Q4.5 6 6 7 L7.5 6 L9.5 8 L8 9.5 Q3.5 9 0.5 2 Z" fill="#c8202f"/></svg>
        555-014-2290
      </li>
      <li>
        <svg viewBox="0 0 10 10" aria-hidden="true"><rect x="0.5" y="2" width="9" height="6" fill="none" stroke="#c8202f"/><path d="M0.5 2 L5 5.5 L9.5 2" fill="none" stroke="#c8202f"/></svg>
        hello@medicrew.com
      </li>
      <li>
        <svg viewBox="0 0 10 10" aria-hidden="true"><circle cx="5" cy="5" r="4.5" fill="none" stroke="#c8202f"/><ellipse cx="5" cy="5" rx="2" ry="4.5" fill="none" stroke="#c8202f"/><path d="M0.5 5 H9.5" stroke="#c8202f"/></svg>
        <span>www.<span class="accent">medicrew</span>.com</span>
      </li>
    </ul>

    <address class="address">145 Harbor Lane<br>Fairview, VA 22030</address>
  </section>
</main>
</body>
</html>
```